Signage setout with photos for side of Mowing Trailer

We need signage for our mowing trailer to attract new business.
Specifically a Rear sign 1470x880mm and Side signs 2400x880mm
Sign needs to be modern and professional.
Some example uploads as to what we have thought about so far.
Logo doesn't need to be the green colour.
Logo words and Logo of Mower do not need to be together.
Link to get a mower image>
https://bluefernmachinery.com/torvo
Updates

Need extra days to review

Target Market(s)

Other Customers driving past the trailer.

Industry/Entity Type

Lawnmowing / Landscaping

Requirements
Must have
• Phone Number, Company Name & Logo, Web address, Linkbook and Insta Logos, Comment - "Acreage & Commercial Specialists" Catchcry - "100% Electric Mowing Company - est 2017" Services "Mowing, Hedging, Pressure Cleaning, Weed Control, Fencing, Turfing, Mulching and Rubbish Removal"
Nice to have
• Full colour background images.

```html
<!DOCTYPE html>
<html lang="en">
<head>
<meta charset="utf-8">
<title>Fresh Meadow Mowing – Trailer Signage</title>
<link rel="stylesheet" href="https://fonts.googleapis.com/css2?family=Bebas+Neue&family=Poppins:wght@400;500;600;700;800&display=swap">
<style>
:root{
  --green-deep:#06351a;
  --green-mid:#0d5a2c;
  --green-field:#167232;
  --lime:#7cd321;
  --orange:#ee6a23;
  --white:#ffffff;
  --sheet-top:#eef0f2;
  --sheet:#c4c4c4;
  --social-a:#2f6fd8;
  --social-b:#d9456f;
}
*{margin:0;padding:0;box-sizing:border-box}
html,body{width:723px;height:1200px;overflow:hidden}
body{background:var(--sheet);position:relative;font-family:'Poppins',sans-serif;color:var(--white)}
.stage-top{position:absolute;left:0;top:0;width:723px;height:512px;background:var(--sheet-top)}

.sign{position:absolute;overflow:hidden;
  background:
    linear-gradient(180deg,rgba(0,0,0,0) 55%,rgba(0,0,0,.28) 100%),
    linear-gradient(180deg,var(--green-mid) 0%,var(--green-field) 48%,var(--green-deep) 100%);
  box-shadow:0 6px 10px rgba(0,0,0,.35)}
.sign *{position:absolute;white-space:nowrap;line-height:1}
.sign .panel-shape{left:0;top:0;width:100%;height:100%}
.photo{border-radius:45%;background:radial-gradient(ellipse at 55% 55%,#8ee02c 0%,#63b81d 38%,rgba(70,70,70,.5) 62%,rgba(255,255,255,0) 76%)}

.headline{font-family:'Bebas Neue',sans-serif;color:var(--white)}
.amp{position:static;font-family:'Poppins',sans-serif;font-weight:300;color:var(--lime);font-size:.5em;margin-left:.25em}
.specialist{background:var(--orange);display:flex;align-items:center;justify-content:center;font-weight:700}
.specialist span{position:static;margin-right:-.55em;letter-spacing:.55em}
.services{list-style:none}
.services li{display:flex;align-items:flex-start;gap:.3em;font-weight:600}
.services li svg{position:static;width:.72em;height:.72em;flex:none;margin-top:.22em}
.services li span{position:static;line-height:1.15}
.pct{font-family:'Bebas Neue',sans-serif;color:var(--lime)}
.electric{font-weight:800;text-transform:uppercase;line-height:.88}
.company{background:var(--orange);font-family:'Bebas Neue',sans-serif;display:flex;align-items:center;justify-content:center}
.company span{position:static;letter-spacing:.32em;margin-right:-.32em}
.est{display:flex;align-items:center;font-weight:500}
.est i{position:static;display:block;height:1px;background:var(--orange);flex:1}
.est b{position:static;font-weight:500;padding:0 .45em;letter-spacing:.06em}
.rule{height:1px;background:var(--lime)}
.phone{display:flex;align-items:center;gap:.2em;font-weight:700}
.phone svg{position:static;width:.78em;height:.78em}
.phone span{position:static}
.web{font-weight:600}
.web em{position:static;font-style:normal;color:var(--orange)}
.follow{font-weight:400}
.social{display:flex;align-items:center;gap:.35em;font-weight:600}
.social i{position:static;display:block;border-radius:50%;flex:none}
.social span{position:static}
.brand{text-align:center;font-weight:700;text-transform:uppercase}
.brand .mark{display:block;border-radius:50%;background:var(--white)}
.brand div{position:static}

/* rear sign, drawn at 603 x 359 */
.sign--rear{width:603px;height:359px}
.sign--rear .photo{left:332px;top:6px;width:255px;height:200px}
.sign--rear .t1{left:30px;top:15px;font-size:68px}
.sign--rear .t2{left:30px;top:67px;font-size:68px}
.sign--rear .specialist{left:27px;top:132px;width:260px;height:24px;font-size:16px}
.sign--rear .services{left:27px;top:162px;font-size:12px}
.sign--rear .pct{left:26px;top:226px;font-size:60px}
.sign--rear .electric{left:132px;top:233px;font-size:23px}
.sign--rear .company{left:276px;top:234px;width:138px;height:32px;font-size:27px}
.sign--rear .est{left:276px;top:269px;width:138px;font-size:12px}
.sign--rear .rule{left:24px;top:289px;width:389px}
.sign--rear .phone{left:26px;top:296px;font-size:34px}
.sign--rear .web{left:26px;top:329px;font-size:11.5px}
.sign--rear .follow{left:276px;top:318px;font-size:10px}
.sign--rear .brand{left:438px;top:232px;width:142px}
.sign--rear .brand .mark{position:static;width:40px;height:40px;margin:0 auto 14px}

/* side sign, drawn at 515 x 188 */
.sign--side{width:515px;height:188px}
.sign--side .photo{left:380px;top:8px;width:125px;height:172px}
.sign--side .brand{left:14px;top:10px;width:56px}
.sign--side .brand .mark{position:static;width:16px;height:16px;margin:0 auto 4px}
.sign--side .pct{left:78px;top:12px;font-size:41px}
.sign--side .electric{left:149px;top:17px;font-size:16px}
.sign--side .company{left:243px;top:18px;width:91px;height:21px;font-size:19px}
.sign--side .est{left:243px;top:42px;width:91px;font-size:8.5px}
.sign--side .t1{left:23px;top:57px;font-size:36px}
.sign--side .t2{left:23px;top:84px;font-size:36px}
.sign--side .specialist{left:21px;top:119px;width:138px;height:13px;font-size:8.5px}
.sign--side .services{left:168px;top:56px;font-size:11.5px}
.sign--side .phone{left:23px;top:146px;font-size:29px}
.sign--side .follow{left:203px;top:148px;font-size:7.5px}
.sign--side .web{left:203px;top:163px;font-size:8.5px}
</style>
</head>
<body>

<div class="stage-top"></div>

<!-- Rear sign, presentation size -->
<section class="sign sign--rear" style="left:60px;top:76px">
  <svg class="panel-shape" viewBox="0 0 603 359" aria-hidden="true">
    <path d="M308,0 H324 Q322,80 345,140 Q312,90 308,0Z" fill="var(--orange)"/>
    <path d="M322,0 H603 V205 Q545,238 455,233 Q338,205 322,0Z" fill="var(--white)"/>
  </svg>
  <div class="photo" role="img" aria-label="Photo of a green electric zero-turn ride-on mower"></div>
  <h1 class="headline t1">ACREAGE<span class="amp">&amp;</span></h1>
  <div class="headline t2">COMMERCIAL</div>
  <div class="specialist"><span>SPECIALIST</span></div>
  <ul class="services">
    <li style="left:0;top:0"><svg viewBox="0 0 10 10"><rect x=".5" y=".5" width="9" height="9" rx="1.5" fill="none" stroke="#7cd321"/><path d="M2.5 5.2l2 2 3.5-4.5" fill="none" stroke="#7cd321" stroke-width="1.4"/></svg><span>Mowing</span></li>
    <li style="left:0;top:17px"><svg viewBox="0 0 10 10"><rect x=".5" y=".5" width="9" height="9" rx="1.5" fill="none" stroke="#7cd321"/><path d="M2.5 5.2l2 2 3.5-4.5" fill="none" stroke="#7cd321" stroke-width="1.4"/></svg><span>Hedging</span></li>
    <li style="left:0;top:34px"><svg viewBox="0 0 10 10"><rect x=".5" y=".5" width="9" height="9" rx="1.5" fill="none" stroke="#7cd321"/><path d="M2.5 5.2l2 2 3.5-4.5" fill="none" stroke="#7cd321" stroke-width="1.4"/></svg><span>Pressure<br>cleaning</span></li>
    <li style="left:85px;top:0"><svg viewBox="0 0 10 10"><rect x=".5" y=".5" width="9" height="9" rx="1.5" fill="none" stroke="#7cd321"/><path d="M2.5 5.2l2 2 3.5-4.5" fill="none" stroke="#7cd321" stroke-width="1.4"/></svg><span>Weed control</span></li>
    <li style="left:85px;top:17px"><svg viewBox="0 0 10 10"><rect x=".5" y=".5" width="9" height="9" rx="1.5" fill="none" stroke="#7cd321"/><path d="M2.5 5.2l2 2 3.5-4.5" fill="none" stroke="#7cd321" stroke-width="1.4"/></svg><span>Fencing</span></li>
    <li style="left:85px;top:34px"><svg viewBox="0 0 10 10"><rect x=".5" y=".5" width="9" height="9" rx="1.5" fill="none" stroke="#7cd321"/><path d="M2.5 5.2l2 2 3.5-4.5" fill="none" stroke="#7cd321" stroke-width="1.4"/></svg><span>Turfing</span></li>
    <li style="left:193px;top:0"><svg viewBox="0 0 10 10"><rect x=".5" y=".5" width="9" height="9" rx="1.5" fill="none" stroke="#7cd321"/><path d="M2.5 5.2l2 2 3.5-4.5" fill="none" stroke="#7cd321" stroke-width="1.4"/></svg><span>Mulching</span></li>
    <li style="left:193px;top:17px"><svg viewBox="0 0 10 10"><rect x=".5" y=".5" width="9" height="9" rx="1.5" fill="none" stroke="#7cd321"/><path d="M2.5 5.2l2 2 3.5-4.5" fill="none" stroke="#7cd321" stroke-width="1.4"/></svg><span>Rubbish<br>Removal</span></li>
  </ul>
  <div class="pct">100%</div>
  <div class="electric">Electric<br>Mowning</div>
  <div class="company"><span>COMPANY</span></div>
  <div class="est"><i></i><b>EST - 2017</b><i></i></div>
  <div class="rule"></div>
  <div class="phone"><svg viewBox="0 0 24 24"><path d="M6.6 2.5l3 3.6-1.8 2.6c1.3 2.9 3.6 5.2 6.5 6.5l2.6-1.8 3.6 3-2 3.6C10.7 20 4 13.3 3 4.5z" fill="#fff"/></svg><span>3904 7126</span></div>
  <div class="web">www.<em>freshmeadowmowing</em>.com.au</div>
  <div class="follow">Follow us on</div>
  <div class="social" style="left:345px;top:302px;font-size:9px"><i style="width:14px;height:14px;background:var(--social-a)"></i><span>Linkbook</span></div>
  <div class="social" style="left:345px;top:322px;font-size:9px"><i style="width:14px;height:14px;background:var(--social-b)"></i><span>Snapview</span></div>
  <div class="brand">
    <i class="mark"></i>
    <div style="font-size:14px">Fresh Meadow</div>
    <div style="font-size:20px;margin-top:2px">Mowing</div>
  </div>
</section>

<!-- Rear sign -->
<section class="sign sign--rear" style="left:105px;top:578px;transform:scale(.8507);transform-origin:0 0">
  <svg class="panel-shape" viewBox="0 0 603 359" aria-hidden="true">
    <path d="M308,0 H324 Q322,80 345,140 Q312,90 308,0Z" fill="var(--orange)"/>
    <path d="M322,0 H603 V205 Q545,238 455,233 Q338,205 322,0Z" fill="var(--white)"/>
  </svg>
  <div class="photo" role="img" aria-label="Photo of a green electric zero-turn ride-on mower"></div>
  <div class="headline t1">ACREAGE<span class="amp">&amp;</span></div>
  <div class="headline t2">COMMERCIAL</div>
  <div class="specialist"><span>SPECIALIST</span></div>
  <ul class="services">
    <li style="left:0;top:0"><svg viewBox="0 0 10 10"><rect x=".5" y=".5" width="9" height="9" rx="1.5" fill="none" stroke="#7cd321"/><path d="M2.5 5.2l2 2 3.5-4.5" fill="none" stroke="#7cd321" stroke-width="1.4"/></svg><span>Mowing</span></li>
    <li style="left:0;top:17px"><svg viewBox="0 0 10 10"><rect x=".5" y=".5" width="9" height="9" rx="1.5" fill="none" stroke="#7cd321"/><path d="M2.5 5.2l2 2 3.5-4.5" fill="none" stroke="#7cd321" stroke-width="1.4"/></svg><span>Hedging</span></li>
    <li style="left:0;top:34px"><svg viewBox="0 0 10 10"><rect x=".5" y=".5" width="9" height="9" rx="1.5" fill="none" stroke="#7cd321"/><path d="M2.5 5.2l2 2 3.5-4.5" fill="none" stroke="#7cd321" stroke-width="1.4"/></svg><span>Pressure<br>cleaning</span></li>
    <li style="left:85px;top:0"><svg viewBox="0 0 10 10"><rect x=".5" y=".5" width="9" height="9" rx="1.5" fill="none" stroke="#7cd321"/><path d="M2.5 5.2l2 2 3.5-4.5" fill="none" stroke="#7cd321" stroke-width="1.4"/></svg><span>Weed control</span></li>
    <li style="left:85px;top:17px"><svg viewBox="0 0 10 10"><rect x=".5" y=".5" width="9" height="9" rx="1.5" fill="none" stroke="#7cd321"/><path d="M2.5 5.2l2 2 3.5-4.5" fill="none" stroke="#7cd321" stroke-width="1.4"/></svg><span>Fencing</span></li>
    <li style="left:85px;top:34px"><svg viewBox="0 0 10 10"><rect x=".5" y=".5" width="9" height="9" rx="1.5" fill="none" stroke="#7cd321"/><path d="M2.5 5.2l2 2 3.5-4.5" fill="none" stroke="#7cd321" stroke-width="1.4"/></svg><span>Turfing</span></li>
    <li style="left:193px;top:0"><svg viewBox="0 0 10 10"><rect x=".5" y=".5" width="9" height="9" rx="1.5" fill="none" stroke="#7cd321"/><path d="M2.5 5.2l2 2 3.5-4.5" fill="none" stroke="#7cd321" stroke-width="1.4"/></svg><span>Mulching</span></li>
    <li style="left:193px;top:17px"><svg viewBox="0 0 10 10"><rect x=".5" y=".5" width="9" height="9" rx="1.5" fill="none" stroke="#7cd321"/><path d="M2.5 5.2l2 2 3.5-4.5" fill="none" stroke="#7cd321" stroke-width="1.4"/></svg><span>Rubbish<br>Removal</span></li>
  </ul>
  <div class="pct">100%</div>
  <div class="electric">Electric<br>Mowning</div>
  <div class="company"><span>COMPANY</span></div>
  <div class="est"><i></i><b>EST - 2017</b><i></i></div>
  <div class="rule"></div>
  <div class="phone"><svg viewBox="0 0 24 24"><path d="M6.6 2.5l3 3.6-1.8 2.6c1.3 2.9 3.6 5.2 6.5 6.5l2.6-1.8 3.6 3-2 3.6C10.7 20 4 13.3 3 4.5z" fill="#fff"/></svg><span>3904 7126</span></div>
  <div class="web">www.<em>freshmeadowmowing</em>.com.au</div>
  <div class="follow">Follow us on</div>
  <div class="social" style="left:345px;top:302px;font-size:9px"><i style="width:14px;height:14px;background:var(--social-a)"></i><span>Linkbook</span></div>
  <div class="social" style="left:345px;top:322px;font-size:9px"><i style="width:14px;height:14px;background:var(--social-b)"></i><span>Snapview</span></div>
  <div class="brand">
    <i class="mark"></i>
    <div style="font-size:14px">Fresh Meadow</div>
    <div style="font-size:20px;margin-top:2px">Mowing</div>
  </div>
</section>

<!-- Side sign -->
<section class="sign sign--side" style="left:105px;top:937px">
  <svg class="panel-shape" viewBox="0 0 515 188" aria-hidden="true">
    <path d="M346,0 H355 Q345,100 450,188 H437 Q334,100 346,0Z" fill="var(--orange)"/>
    <path d="M355,0 H515 V188 H450 Q345,100 355,0Z" fill="var(--white)"/>
  </svg>
  <div class="photo" role="img" aria-label="Photo of a green electric zero-turn ride-on mower"></div>
  <div class="brand">
    <i class="mark"></i>
    <div style="font-size:5.5px">Fresh Meadow</div>
    <div style="font-size:7.5px;margin-top:1px">Mowing</div>
  </div>
  <div class="pct">100%</div>
  <div class="electric">Electric<br>Mowning</div>
  <div class="company"><span>COMPANY</span></div>
  <div class="est"><i></i><b>EST - 2017</b><i></i></div>
  <div class="headline t1">ACREAGE<span class="amp">&amp;</span></div>
  <div class="headline t2">COMMERCIAL</div>
  <div class="specialist"><span>SPECIALIST</span></div>
  <ul class="services">
    <li style="left:0;top:0"><svg viewBox="0 0 10 10"><rect x=".5" y=".5" width="9" height="9" rx="1.5" fill="none" stroke="#7cd321"/><path d="M2.5 5.2l2 2 3.5-4.5" fill="none" stroke="#7cd321" stroke-width="1.4"/></svg><span>Mowing</span></li>
    <li style="left:0;top:15.5px"><svg viewBox="0 0 10 10"><rect x=".5" y=".5" width="9" height="9" rx="1.5" fill="none" stroke="#7cd321"/><path d="M2.5 5.2l2 2 3.5-4.5" fill="none" stroke="#7cd321" stroke-width="1.4"/></svg><span>Hedging</span></li>
    <li style="left:0;top:31px"><svg viewBox="0 0 10 10"><rect x=".5" y=".5" width="9" height="9" rx="1.5" fill="none" stroke="#7cd321"/><path d="M2.5 5.2l2 2 3.5-4.5" fill="none" stroke="#7cd321" stroke-width="1.4"/></svg><span>Pressure<br>cleaning</span></li>
    <li style="left:0;top:61px"><svg viewBox="0 0 10 10"><rect x=".5" y=".5" width="9" height="9" rx="1.5" fill="none" stroke="#7cd321"/><path d="M2.5 5.2l2 2 3.5-4.5" fill="none" stroke="#7cd321" stroke-width="1.4"/></svg><span>Mulching</span></li>
    <li style="left:77px;top:0"><svg viewBox="0 0 10 10"><rect x=".5" y=".5" width="9" height="9" rx="1.5" fill="none" stroke="#7cd321"/><path d="M2.5 5.2l2 2 3.5-4.5" fill="none" stroke="#7cd321" stroke-width="1.4"/></svg><span>Weed control</span></li>
    <li style="left:77px;top:15.5px"><svg viewBox="0 0 10 10"><rect x=".5" y=".5" width="9" height="9" rx="1.5" fill="none" stroke="#7cd321"/><path d="M2.5 5.2l2 2 3.5-4.5" fill="none" stroke="#7cd321" stroke-width="1.4"/></svg><span>Fencing</span></li>
    <li style="left:77px;top:31px"><svg viewBox="0 0 10 10"><rect x=".5" y=".5" width="9" height="9" rx="1.5" fill="none" stroke="#7cd321"/><path d="M2.5 5.2l2 2 3.5-4.5" fill="none" stroke="#7cd321" stroke-width="1.4"/></svg><span>Turfing</span></li>
    <li style="left:77px;top:46.5px"><svg viewBox="0 0 10 10"><rect x=".5" y=".5" width="9" height="9" rx="1.5" fill="none" stroke="#7cd321"/><path d="M2.5 5.2l2 2 3.5-4.5" fill="none" stroke="#7cd321" stroke-width="1.4"/></svg><span>Rubbish<br>Removal</span></li>
  </ul>
  <div class="phone"><svg viewBox="0 0 24 24"><path d="M6.6 2.5l3 3.6-1.8 2.6c1.3 2.9 3.6 5.2 6.5 6.5l2.6-1.8 3.6 3-2 3.6C10.7 20 4 13.3 3 4.5z" fill="#fff"/></svg><span>3904 7126</span></div>
  <div class="follow">Follow us on</div>
  <div class="social" style="left:250px;top:146px;font-size:6.5px"><i style="width:10px;height:10px;background:var(--social-a)"></i><span>Linkbook</span></div>
  <div class="social" style="left:293px;top:146px;font-size:6.5px"><i style="width:10px;height:10px;background:var(--social-b)"></i><span>Snapview</span></div>
  <div class="web">www.<em>freshmeadowmowing</em>.com.au</div>
</section>

</body>
</html>
```